Word Template for KOREL Polls

KOREL Polls stands for 'Kindred Outlook Readings Entered Locally Polls'. It is a collaborative research effort to format and combine multiple sources of public opinion data from around the world into merged datasets. We need a Microsoft Word template design for our research reports, dataset codebooks, crowdsourced development guidelines, and other documents that will be produced as part of the research and development. The template should match the website design and logo, which are attached to this contest (these are the files from previous successful design contests).

The main purpose will be to write reports discussing research and analysis. There will be lots data visualizations (bar charts, scatter plots, pie charts, histograms, trend line charts etc.) as well as tables, diargams, and photos mixed in wit all the text. A second purpose will be to write guidebooks to describe processes and teach others how to manage data, find variables, and write code, which will include screenshots and Word are diagrams and figures.

There are some document uploaded as examples for the kinds of things for which we need the template (working papers, codebooks, pamphlets, etc)

Target Market(s)

academia, government, non-profits, postgraduates, researchers

Font styles to use
Serif

Colors

Designer to choose colors to be used in the design.

Requirements
Must have
• A4 size page template
• Cover page
• Must match website design and logo (see attached)
Nice to have
• Colors to match logo and website (see attached)

```html
<!DOCTYPE html>
<html lang="en">
<head>
<meta charset="utf-8">
<title>KOREL Polls – Report Template Pages</title>
<link rel="stylesheet" href="https://fonts.googleapis.com/css2?family=Open+Sans:wght@300;400;600;700&display=swap">
<style>
:root{
  --bg:#c9c9c9;
  --paper:#ffffff;
  --blue:#1b79c9;
  --blue-dark:#0f5fa8;
  --blue-soft:#9cc8ea;
  --blue-pale:#d6e9f8;
  --row:#cfe5f6;
  --ink:#3a3a3a;
  --ink-soft:#6a6a6a;
  --rule:#b9d3ea;
}
*{box-sizing:border-box;margin:0;padding:0}
html,body{width:1200px;height:1200px;overflow:hidden}
body{background:var(--bg);font-family:"Open Sans",Arial,sans-serif;color:var(--ink);position:relative}
.page{position:absolute;width:258px;height:364px;background:var(--paper);box-shadow:0 2px 5px rgba(0,0,0,.25);overflow:hidden}
.c1{left:44px}.c2{left:326px}.c3{left:608px}.c4{left:890px}
.r1{top:32px}.r2{top:418px}.r3{top:805px}
.runhead{position:absolute;left:30px;right:24px;top:20px;height:16px;border-top:1px dotted var(--blue);border-bottom:1px dotted var(--blue);display:flex;align-items:center;justify-content:center}
.runhead h2{font-weight:400;font-size:8.4px;letter-spacing:.2px;color:#333}
.body{position:absolute;left:30px;right:24px;top:44px}
.sub{font-size:6.6px;font-weight:600;color:#333;margin:5px 0 2px}
.kicker{font-size:3.8px;color:var(--blue);margin-top:3px}
.p{font-size:3.5px;line-height:1.55;color:var(--ink);margin-bottom:4px}
.p.blue{color:var(--blue)}
.p.center{text-align:center}
.folio{position:absolute;left:0;right:0;bottom:7px;height:7px;display:flex;align-items:center}
.folio-url{background:var(--blue);color:#fff;font-size:3.2px;height:5px;line-height:5px;padding-left:20px;width:160px;clip-path:polygon(0 0,100% 0,96% 100%,0 100%)}
.folio-brand{display:flex;align-items:center;gap:2px;margin-left:8px;font-size:4.6px;font-weight:600;color:var(--blue)}
.dot{width:4px;height:4px;border-radius:50%;background:var(--blue);display:inline-block}
.folio-num{margin-left:auto;margin-right:6px;background:var(--blue);color:#fff;font-size:3.8px;font-weight:600;width:18px;height:7px;display:flex;align-items:center;justify-content:center}
/* cover */
.cover-brand{position:absolute;top:32px;left:0;right:0;display:flex;justify-content:center;align-items:center;gap:6px;font-size:17px;font-weight:600;color:var(--blue)}
.cover-brand .dot{width:12px;height:12px}
.cover-deco{position:absolute;left:-70px;top:110px;width:150px;height:150px;border-radius:50%;background:var(--blue-pale)}
.cover-title{position:absolute;top:289px;left:0;right:0;text-align:center}
.cover-title .l1{font-size:12.4px;font-weight:700;color:var(--blue)}
.cover-title .l2{font-size:12.4px;font-weight:600;color:#555;margin-top:-2px}
.cover-title .l3{font-size:5.6px;font-weight:700;color:var(--blue);margin-top:12px}
/* toc */
.toc-head{font-size:7px;font-weight:600;color:var(--blue);margin-bottom:8px}
.toc li{list-style:none;display:flex;font-size:3.8px;line-height:8.6px}
.toc .dots{flex:1;border-bottom:1px dotted #999;margin:0 4px 3px}
/* vision band */
.band{display:flex;align-items:center;gap:6px;background:var(--blue);padding:3px 6px;margin-bottom:6px}
.band svg{flex:none}
.band .p{color:#fff;margin:0;font-size:4.4px;line-height:1.3}
/* tables */
.tbl{width:100%;border-collapse:separate;border-spacing:1px 1.5px;font-size:3.4px;margin:4px 0 6px}
.tbl th{background:var(--blue);color:#fff;font-weight:600;height:6px}
.tbl td{background:#eef5fb;height:5.5px;padding:0 3px}
.tbl td.n{text-align:center}
.tbl tr.phase td{background:var(--row);color:var(--blue-dark);font-weight:600}
.tbl tr.tot td{background:#dde3e8;font-weight:700}
.tbl tr.grand td{background:var(--blue);color:#fff;font-weight:600}
.grid-tbl{position:absolute;left:30px;right:24px;top:46px;height:264px;border:1px solid var(--rule)}
.grid-tbl .gh{display:flex;background:var(--blue);color:#fff;font-size:5px;height:9px;align-items:center}
.grid-tbl .gh span{flex:1;padding-left:10px}
.grid-tbl .lines{height:254px;background:repeating-linear-gradient(to bottom,#fff 0 8.5px,var(--rule) 8.5px 9px);position:relative}
.grid-tbl .lines::after{content:"";position:absolute;left:50%;top:0;bottom:0;border-left:1px solid var(--rule)}
.photo{background:linear-gradient(135deg,#2c3d52,#6b7f93 55%,#c6b49a);}
.bul{font-size:3.4px;line-height:1.55;margin-bottom:3px}
.bul.sq::before{content:"■ ";color:var(--blue-dark)}
.bul.tri{padding-left:8px;color:var(--blue)}
.bul.tri::before{content:"▶ ";}
/* back */
.back-deco{position:absolute;right:-60px;top:95px;width:170px;height:170px;border-radius:50%;background:var(--blue-pale)}
.back-foot{position:absolute;left:28px;right:20px;bottom:30px;display:flex;align-items:center;gap:10px}
.back-brand{display:flex;align-items:center;gap:3px;font-size:7px;font-weight:600;color:var(--blue)}
.back-brand .dot{width:6px;height:6px}
.contact{font-size:3px;line-height:1.6;color:#555}
.contact b{color:var(--blue)}
</style>
</head>
<body>

<!-- Cover -->
<section class="page c1 r1">
  <div class="cover-brand"><i class="dot"></i>KOREL Polls</div>
  <div class="cover-deco"></div>
  <div class="cover-title">
    <div class="l1">LOREM IPSUM IS SIMPLY</div>
    <div class="l2">DUMMY HAS BEEN</div>
    <div class="l3">LOREM IPSUM IS SIMPLY DUMMY HAS BEEN</div>
  </div>
</section>

<!-- Table of contents -->
<section class="page c2 r1">
  <header class="runhead"><h2>TABLE OF CONTENTS</h2></header>
  <div class="body" style="top:48px">
    <div class="toc-head">Contents</div>
    <ul class="toc">
      <li>Table of Contents<span class="dots"></span>01</li>
      <li>Executive Summary<span class="dots"></span>02</li>
      <li>Our Understanding of Your Needs<span class="dots"></span>02</li>
      <li>Our Recommendations<span class="dots"></span>03</li>
      <li>Our Approach<span class="dots"></span>05</li>
      <li>Budget and Timeframe<span class="dots"></span>07</li>
      <li>Appendix A: About Marlow Bend<span class="dots"></span>10</li>
      <li>Appendix B: Selected Client List<span class="dots"></span>10</li>
      <li>Appendix C: Our Capabilities<span class="dots"></span>11</li>
      <li>Appendix D: Our Process<span class="dots"></span>12</li>
    </ul>
  </div>
  <footer class="folio"><span class="folio-url">www.korelpolls.org</span><span class="folio-brand"><i class="dot"></i>KOREL Polls</span><span class="folio-num">01</span></footer>
</section>

<!-- Vision -->
<section class="page c3 r1">
  <header class="runhead"><h2>VISION</h2></header>
  <div class="body">
    <div class="band">
      <svg width="18" height="18" viewBox="0 0 18 18" aria-hidden="true"><circle cx="9" cy="9" r="8" fill="#fff"/><circle cx="9" cy="9" r="5.5" fill="none" stroke="#1b79c9" stroke-width="1.3"/><circle cx="9" cy="9" r="2.5" fill="#1b79c9"/></svg>
      <p class="p">Tallyna's mission is to help and support the self-employed and small business owners with their administrative tasks so they can focus on what matters – their business.</p>
    </div>
    <p class="p blue">Administrative tasks are cumbersome, time-consuming and often prevent small owners from focusing their time and energy on their business and their customers. They can also be extremely stressful for those attempting these tasks for the first time.</p>
    <p class="p center">At Tallyna, we envisage accounting for the self-employed and small business owners as being <span style="color:var(--blue)">automated and decentralized</span></p>
    <p class="p">Accounting can and should be done automatically. By connecting to all sources of accounting data such as bank accounts, payment systems, e-commerce websites, and invoicing systems, Tallyna AI automatically completes these tasks, which would take hours to do manually. Bookings are created automatically and fully completed. Financial statements are available within a couple of clicks, and after analysing your data, Tallyna AI will offer you tips to improve your financial stability.</p>
    <p class="p">What may seem like a pipedream to the millions of self-employed who struggle with their admin, is already a reality. Now is the time to join Tallyna on its mission to transform the world of bookkeeping through the power of AI.</p>
    <div class="sub">The Tallyna model</div>
    <p class="p">Tallyna is based on an innovative license model that uses Token-as-a-License (TaaL). The token represents lifelong software license for Tallyna solutions. The Pre-ICO token sales will enable Tallyna to complete its development of Tallyna AI to deliver fully automatic bookkeeping.</p>
    <p class="p">The Pre-ICO token sale will also pave the way for a future Tallyna ICO. Tallyna will launch accounting on the blockchain and ensure your accounting data is comprehensive and private, but available everywhere within your preferred apps. It will empower you to manage your data as you see fit in a fully decentralized way. Furthermore, a new range of business apps will connect to Tallyna to provide you with leading edge business data access to ensure you have the best available data at your fingertips.</p>
    <p class="p">Tallyna supports strong data ownership laws that truly protect individuals and ensure they have complete ownership of their data. Through decentralisation Tallyna helps to ensure you always have full ownership of your data to decide how it should be used.</p>
    <p class="p">To find out more about the Tallyna AI project, and the Tallyna TaaL or if you are interested in purchasing Tallyna TaaL, please register with your email at <span style="color:var(--blue);text-decoration:underline">https://www.tallyna.example/en/ico</span> so we</p>
  </div>
  <footer class="folio"><span class="folio-url">www.korelpolls.org</span><span class="folio-brand"><i class="dot"></i>KOREL Polls</span><span class="folio-num">03</span></footer>
</section>

<!-- Headline: solution -->
<section class="page c4 r1">
  <header class="runhead"><h2>HEADLINE HERE</h2></header>
  <div class="body">
    <div class="sub" style="margin-top:4px">Solution</div>
    <div class="kicker">AI automated accounting</div>
    <p class="p">Tallyna builds automation in stages on top of its current system to reach full automation thanks to the Tallyna AI. Tallyna AI automates every manual task performed by the user. It starts by connecting to all sources of accounting data such as bank accounts, credit card, webshop or document management systems. Based on these data, Tallyna AI creates bookings and generates financial reports. Finally, Tallyna AI features chat-like interface that allows users to communicate seamlessly with it, viewing it as a trusted advisor over time for all their accounting queries.</p>
    <div class="kicker">Blockchain software license or Token-as-a-License (TaaL)</div>
    <p class="p">It is possible to create tokens on blockchain that represent software licenses, also known as Token-as-a-Licence (TaaL). Tallyna creates TaaL by using the Kestrel official wallet which interacts with the Kestrel blockchain. Upon purchase of TaaL, the token holder is free to transfer or sell TaaL using secondary market that is built directly over the blockchain, in our case, the Kestrel marketplace. Tallyna checks the validity of a token against the blockchain ensuring that token holders have access to the software. TaaL make distribution and securisation of software licenses easier for software developers. It also makes the management and resale of software license easier for software owners. All in all, TaaL has a higher value as a normal software license.</p>
    <div class="sub">Pre-ICO Token sale</div>
    <p class="p">To realize this innovative vision, Tallyna is launching a pre-ICO in form of a token sale on Kestrel blockchain. 20,000,000 tokens are available to purchase for the price of CRD 0.10 each during a 30-day period to be announced. Tokens represent Tallyna lifelong software licenses and by purchasing enough tokens, holders gain access to Tallyna software. 15,000 tokens give access to Tallyna invoicing or accounting. 20,000 tokens give access to both Tallyna accounting and invoicing. Future customers will still have the opportunity to buy directly yearly or monthly subscriptions to have access to Tallyna.</p>
    <div class="sub">Future plans</div>
    <p class="p">A future ICO is planned between 18 and 24 months after the pre-ICO token sale. This offering will support the development of Tallyna into a fully decentralized, privacy-focused ecosystem of applications. The new model will reward each participant so that a new world with zero administrative tasks becomes reality.</p>
  </div>
  <footer class="folio"><span class="folio-url">www.korelpolls.org</span><span class="folio-brand"><i class="dot"></i>KOREL Polls</span><span class="folio-num">02</span></footer>
</section>

<!-- Headline: chart -->
<section class="page c1 r2">
  <header class="runhead"><h2>HEADLINE HERE</h2></header>
  <div class="body">
    <svg width="204" height="100" viewBox="0 0 204 100" style="margin:6px 0 2px 18px" role="img" aria-label="Monthly bar chart, January to December">
      <g fill="#3d8fd6">
        <rect x="4" y="42" width="11" height="51"/><rect x="17" y="32" width="11" height="61"/><rect x="30" y="53" width="11" height="40"/>
        <rect x="43" y="71" width="11" height="22"/><rect x="56" y="88" width="11" height="5"/><rect x="69" y="72" width="11" height="21"/>
        <rect x="82" y="84" width="11" height="9"/><rect x="95" y="74" width="11" height="19"/><rect x="108" y="70" width="11" height="23"/>
        <rect x="121" y="47" width="11" height="46"/><rect x="134" y="39" width="11" height="54"/><rect x="147" y="14" width="11" height="79"/>
      </g>
      <g font-size="3.4" fill="#444" text-anchor="middle">
        <text x="9.5" y="40">122</text><text x="22.5" y="30">146</text><text x="35.5" y="51">96</text><text x="48.5" y="69">53</text>
        <text x="61.5" y="86">11</text><text x="74.5" y="70">50.5</text><text x="87.5" y="82">20.9</text><text x="100.5" y="72">46</text>
        <text x="113.5" y="68">55</text><text x="126.5" y="45">109</text><text x="139.5" y="37">129</text><text x="152.5" y="12">189</text>
        <text x="9.5" y="98">Jan</text><text x="22.5" y="98">Febr</text><text x="35.5" y="98">March</text><text x="48.5" y="98">April</text>
        <text x="61.5" y="98">May</text><text x="74.5" y="98">Jun</text><text x="87.5" y="98">July</text><text x="100.5" y="98">Aug</text>
        <text x="113.5" y="98">Sep</text><text x="126.5" y="98">Oct</text><text x="139.5" y="98">Nov</text><text x="152.5" y="98">Dec</text>
      </g>
      <line x1="2" y1="93" x2="162" y2="93" stroke="#999" stroke-width=".4"/>
    </svg>
    <p class="p blue" style="margin-top:10px">Administrative tasks are cumbersome, time-consuming and often prevent small owners from focusing their time and energy on their business and their customers. They can also be extremely stressful and nerve-wracking for those attempting these tasks for the first time.</p>
    <p class="p center">At Tallyna, we envisage accounting for the self-employed and small business owners as being <span style="color:var(--blue)">automated and decentralized</span></p>
    <p class="p">Accounting can and should be done automatically. By connecting to all sources of accounting data such as bank accounts, payment systems, e-commerce websites, and invoicing systems, Tallyna AI automatically completes these tasks, which would take hours to do manually. Bookings are created automatically and fully completed. Financial statements are available within a couple of clicks, and after analysing your data, Tallyna AI will offer you tips to improve your financial stability.</p>
    <p class="p">What may seem like a pipedream to the millions of self-employed who struggle with their admin, is already a reality. Now is the time to join Tallyna on its mission to transform the world of bookkeeping through the power of AI.</p>
    <div class="sub">The Tallyna model</div>
    <p class="p">Tallyna is based on an innovative license model that uses Token-as-a-License (TaaL). The token represents lifelong software license for Tallyna solutions. The Pre-ICO token sales will enable Tallyna to complete its development of Tallyna AI to deliver fully automatic bookkeeping.</p>
    <p class="p">The Pre-ICO token sale will also pave the way for a future Tallyna ICO. Tallyna will launch</p>
  </div>
  <footer class="folio"><span class="folio-url">www.korelpolls.org</span><span class="folio-brand"><i class="dot"></i>KOREL Polls</span><span class="folio-num">09</span></footer>
</section>

<!-- Budget and timeframe -->
<section class="page c2 r2">
  <header class="runhead"><h2>BUDGET AND TIMEFRAME</h2></header>
  <div class="body" style="top:42px">
    <div class="sub">Implementation Estimate</div>
    <p class="p">The bulk of the implementation costs will be defined by discovery. Based on similar CRM implementation projects, we feel expect that the CRM side will be something that falls between 200 and 300 hours, give or take. The wide swing in hours in phase one is related to the ill-understood nature of both the integration needs and our role in the integration project. Our focus in discovery (as mentioned above) will be to nail down those requirements and our role as it relates to what is needed to integrate the sites with the CRM.</p>
    <table class="tbl">
      <tr><th style="width:52%">Task</th><th>Hours</th><th>Cost</th></tr>
      <tr><td>Discovery</td><td class="n">40</td><td class="n">$8,000</td></tr>
      <tr class="phase"><td>Phase 1</td><td></td><td></td></tr>
      <tr><td>Discovery</td><td class="n">20-40</td><td class="n">$8,000</td></tr>
      <tr><td>Discovery</td><td class="n">20-40</td><td class="n">$8,000</td></tr>
      <tr><td>Discovery</td><td class="n">20-40</td><td class="n">$8,000</td></tr>
      <tr class="tot"><td>Total Phase 1</td><td class="n">80-240</td><td class="n">$16,800-40,000</td></tr>
      <tr class="phase"><td>Phase 2</td><td></td><td></td></tr>
      <tr><td>Discovery</td><td class="n">20-40</td><td class="n">$8,000</td></tr>
      <tr class="tot"><td>Total Phase 2</td><td class="n">80-240</td><td class="n">$16,800-40,000</td></tr>
      <tr class="grand"><td>Total Estimated Implementation Cost</td><td class="n">220-480</td><td class="n">$44,000-96,000</td></tr>
    </table>
    <div class="sub">Project Timeline</div>
    <p class="p">Based on the information we have set out our disposal, the March 21st launch date doesn't seem a realistic goal to get both the work done needed to provide the foundation for the future CRM instance and the integration given the state of apparent flux of the requirements. That said, we feel it prudent to proceed with discovery before committing to or receiving the estimates. We are currently estimating that the first phase will take somewhere between 7 and 12 weeks (including discovery) to complete.</p>
    <table class="tbl">
      <tr><th style="width:62%">Task</th><th>Weeks to Complete</th></tr>
      <tr><td>Discovery</td><td class="n">1-2</td></tr>
      <tr><td>Phase 1</td><td class="n">6-10</td></tr>
      <tr><td>Phase 2</td><td class="n">8-12</td></tr>
      <tr class="tot"><td>Total Number of Weeks</td><td></td></tr>
    </table>
  </div>
  <footer class="folio"><span class="folio-url">www.korelpolls.org</span><span class="folio-brand"><i class="dot"></i>KOREL Polls</span><span class="folio-num">04</span></footer>
</section>

<!-- Headline: blank table -->
<section class="page c3 r2">
  <header class="runhead"><h2>HEADLINE HERE</h2></header>
  <div class="grid-tbl">
    <div class="gh"><span>Lorem ipsum</span><span>Lorem ipsum</span></div>
    <div class="lines"></div>
  </div>
  <footer class="folio"><span class="folio-url">www.korelpolls.org</span><span class="folio-brand"><i class="dot"></i>KOREL Polls</span><span class="folio-num">08</span></footer>
</section>

<!-- Headline: photo -->
<section class="page c4 r2">
  <header class="runhead"><h2>HEADLINE HERE</h2></header>
  <div class="body">
    <div class="photo" role="img" aria-label="Photo of a stressed business owner at a desk with a colleague's hand on his shoulder" style="height:92px;margin-bottom:8px"></div>
    <p class="p blue">Tallyna's mission is to help and support the self-employed and small business owners with their administrative tasks so they can focus on what matters – their business.</p>
    <p class="p">Administrative tasks are cumbersome, time-consuming and often prevent small owners from focusing their time and energy on their business and their customers. They can also be extremely stressful and nerve-wracking for those attempting these tasks for the first time.</p>
    <p class="p">At Tallyna, we envisage accounting for the self-employed and small business owners as being <span style="color:var(--blue)">automated and decentralized</span></p>
    <p class="p">Accounting can and should be done automatically. By connecting to all sources of accounting data such as bank accounts, payment systems, e-commerce websites, and invoicing systems, Tallyna AI automatically completes these tasks, which would take hours to do manually. Bookings are created automatically and fully completed. Financial statements are available within a couple of clicks, and after analysing your data, Tallyna AI will offer you tips to improve your financial stability.</p>
    <p class="p">What may seem like a pipedream to the millions of self-employed who struggle with their admin, is already a reality. Now is the time to join Tallyna on its mission to transform the world of bookkeeping through the power of AI.</p>
    <div class="sub">The Tallyna model</div>
    <p class="p">Tallyna is based on an innovative license model that uses Token-as-a-License (TaaL). The token represents lifelong software license for Tallyna solutions. The Pre-ICO token sales will enable Tallyna to complete its development of Tallyna AI to deliver fully automatic bookkeeping.</p>
    <p class="p">with leading edge business data access to ensure you have the best available data at your fingertips.</p>
  </div>
  <footer class="folio"><span class="folio-url">www.korelpolls.org</span><span class="folio-brand"><i class="dot"></i>KOREL Polls</span><span class="folio-num">06</span></footer>
</section>

<!-- Our understanding -->
<section class="page c1 r3">
  <header class="runhead"><h2>OUR UNDERSTANDING OF YOUR NEEDS</h2></header>
  <div class="body">
    <p class="p">In the last two weeks of January 2014 we conducted high level conversations both with your staff and your technology partner Loomwright. As a result of those conversations we've been able to gather the following high level goals for your project:</p>
    <p style="font-size:5.6px;color:#666;line-height:1.2;margin:5px 0 4px">FieldDesk must be in place to support StrideNet at launch and as the program evolves</p>
    <p class="p" style="color:var(--blue);font-weight:600">The most critical aspect of this implementation both in terms of time sensitivity as well as functionality is centered around the support for the StrideNet project. Our current understanding of this project and how it relates to FieldDesk is as follows:</p>
    <div class="bul sq">StrideNet will be comprised of a series of websites focused on organizing institutions and individuals within six specific community sectors with the goal of increased institutional and public support to help communities become better prepared to minimize the risks and maximize opportunities of changing climate.</div>
    <div class="bul sq">The primary goals of the CRM application are:</div>
    <div class="bul tri">capture information of individuals and organizations (along with their respective roles)</div>
    <div class="bul tri">track their progress on their site specific to-do lists and site interactions</div>
    <div class="bul tri">allow greenCivic to push out next steps (ideally in an automated style) related to their to-do list progress and online interactions</div>
    <div class="bul tri">infuse greenCivic's online and offline marketing program with useful segmentation information</div>
    <div class="bul tri">natively integrate with both the StrideNet family of sites as well as greenCivic's email service provider of choice</div>
    <div class="bul sq">The data architecture must be well defined but flexible to support the core needs of the sites at launch as well as anticipated needs in the future.</div>
    <div class="bul tri">For instance, the faith based site may collect a "denomination" field, while other sites may not collect that field.</div>
    <div class="bul tri">Future interactions outside of the to-do list may become necessary to track and greenCivic will need a systemic way to capture those interactions, be able to segment on them and potentially provide automated marketing around those similar to the to-do list</div>
    <div class="bul sq">The information collected from the StrideNet sites must be combined with current information held within greenCivic and provide a holistic view of institutions and individuals.</div>
  </div>
  <footer class="folio"><span class="folio-url">www.korelpolls.org</span><span class="folio-brand"><i class="dot"></i>KOREL Polls</span><span class="folio-num">05</span></footer>
</section>

<!-- Headline: two photos -->
<section class="page c2 r3">
  <header class="runhead"><h2>HEADLINE HERE</h2></header>
  <div class="photo" role="img" aria-label="Photo of a tired man in a suit holding his forehead" style="position:absolute;left:29px;top:46px;width:87px;height:118px"></div>
  <div class="photo" role="img" aria-label="Photo of a man working at a laptop in a dim office" style="position:absolute;left:29px;top:205px;width:87px;height:120px;background:linear-gradient(135deg,#3a2f2a,#7d6a5c 55%,#c9c1b3)"></div>
  <div style="position:absolute;left:128px;right:28px;top:46px">
    <p class="p blue">Tallyna's mission is to help and support the self-employed and small business owners with their administrative tasks so they can focus on what matters – their business.</p>
    <p class="p">Administrative tasks are cumbersome, time-consuming and often prevent small owners from focusing their time and energy on their business and their customers. They can also be extremely stressful and nerve-wracking for those attempting these tasks for the first time.</p>
    <p class="p">At Tallyna, we envisage accounting for the self-employed and small business owners as being <span style="color:var(--blue)">automated and decentralized</span></p>
    <p class="p">Accounting can and should be done automatically. By connecting to all sources of accounting data such as bank accounts, payment systems, e-commerce websites, and invoicing systems, Tallyna AI automatically completes these tasks, which would take hours to do manually. Bookings are created automatically and fully completed. Financial statements are available within a couple of clicks, and after analysing your data, Tallyna AI will offer you tips to improve your financial stability.</p>
    <p class="p">What may seem like a pipedream to the millions of self-employed who struggle with</p>
    <div class="sub" style="color:var(--blue)">The Tallyna model</div>
    <p class="p">Tallyna is based on an innovative license model that uses Token-as-a-License (TaaL). The token represents lifelong software license for Tallyna solutions. The Pre-ICO token sales will enable Tallyna to complete its development of Tallyna AI to deliver fully automatic bookkeeping.</p>
  </div>
  <footer class="folio"><span class="folio-url">www.korelpolls.org</span><span class="folio-brand"><i class="dot"></i>KOREL Polls</span><span class="folio-num">07</span></footer>
</section>

<!-- Back cover -->
<section class="page c3 r3">
  <div class="back-deco"></div>
  <div class="back-foot">
    <div class="back-brand"><i class="dot"></i>KOREL Polls</div>
    <div class="contact"><b>☎</b> 000-555-0142 Ext 101<br><b>✉</b> hello@korelpolls.org<br><b>●</b> www.korelpolls.org</div>
    <div class="contact">300, 1055 West Harbour Street<br>Lakeview, Northshire LK1 2X4</div>
  </div>
</section>

</body>
</html>
```